The Brightway Surgery Stationary (Medical)

Stationery for The Brightway surgery
using existing logos
Please also add a green apple if possible on another corner away from the logo on some of your designs

Please take a look at www.thebrightwaysurgery.com.au so you can get a feel for what The Brightway Surgery offers our clients.

Stationary Required: business cards, letter head, comp slips

I do not require envelopes or invoives.

Target Market(s)

The general popultation needing medical care
Professionals
Mums & Dads
Elderly

Industry/Entity Type

Business

Requirements
Must have
• Company Logo

Address
Email
Website
Phone
Should not have
• Traditional Medical Icons
No Times New Roman

```html
<!DOCTYPE html>
<html lang="en">
<head>
<meta charset="utf-8">
<title>The Brightway Surgery Stationery</title>
<link href="https://fonts.googleapis.com/css2?family=Arimo:wght@400;700&display=swap" rel="stylesheet">
<style>
  :root {
    --green: #8cd31f;
    --blue: #5ccbe8;
    --pale-green: #f0f8e6;
    --pale-blue: #e6f6fb;
    --ink: #1e1e1e;
    --grey: #8a8a8a;
    --paper: #ffffff;
    --stage: #ffffff;
  }
  * { box-sizing: border-box; margin: 0; padding: 0; }
  html, body { width: 1200px; height: 900px; overflow: hidden; background: var(--stage); }
  body { position: relative; font-family: "Arimo", Arial, sans-serif; color: var(--ink); }

  .sheet {
    position: absolute; background: var(--paper); overflow: hidden;
    box-shadow: 0 1px 4px rgba(0,0,0,.25);
  }
  .sheet > svg.decor { position: absolute; inset: 0; width: 100%; height: 100%; }

  .brand { position: absolute; display: flex; flex-direction: column; align-items: flex-start; }
  .brand__row { display: flex; align-items: center; gap: 8px; }
  .brand__dot { width: 22px; height: 22px; border-radius: 50%; background: var(--blue); flex: none; }
  .brand__name { color: var(--green); font-weight: 700; font-size: 17px; line-height: 1.1; white-space: nowrap; }
  .brand__tagline { color: var(--grey); font-size: 9px; margin-left: 30px; margin-top: 3px; line-height: 1.25; white-space: nowrap; }

  .contact { position: absolute; font-size: 11px; font-weight: 700; line-height: 1.65; text-align: right; white-space: nowrap; }

  /* Letterhead */
  .letterhead { left: 28px; top: 48px; width: 552px; height: 784px; }
  .letterhead .brand { right: 36px; top: 40px; }
  .letterhead .contact { right: 36px; top: 106px; }
  .letterhead__footer {
    position: absolute; left: 0; right: 0; bottom: 0; height: 78px; background: var(--green);
    color: var(--paper); font-size: 11px; line-height: 1.55; text-align: center;
    display: flex; flex-direction: column; justify-content: center;
  }

  /* Business card: details side */
  .card-details { left: 668px; top: 96px; width: 498px; height: 190px; }
  .card-details .brand { left: 16px; top: 52px; }
  .card-details .brand__name { font-size: 15px; }
  .card-details__rule { position: absolute; left: 172px; top: 40px; width: 2px; height: 96px; background: var(--green); }
  .card-details__text { position: absolute; left: 186px; top: 40px; font-size: 9.5px; font-weight: 700; line-height: 1.5; white-space: nowrap; }
  .card-details__text p + p { margin-top: 8px; }
  .card-details__band { position: absolute; left: 0; right: 0; bottom: 0; height: 14px; background: var(--green); }

  /* Business card: logo side */
  .card-front { left: 668px; top: 310px; width: 498px; height: 256px; }
  .card-front .brand { left: 178px; top: 96px; }

  /* Compliments slip */
  .comp-slip { left: 604px; top: 588px; width: 558px; height: 268px; }
  .comp-slip__title { position: absolute; left: 24px; top: 24px; font-size: 10px; letter-spacing: 2px; }
  .comp-slip .brand { right: 30px; top: 26px; }
  .comp-slip .contact { right: 30px; top: 96px; font-size: 10px; }
  .comp-slip__address { position: absolute; left: 0; right: 0; bottom: 22px; text-align: center; font-size: 10px; font-weight: 700; line-height: 1.6; }
</style>
</head>
<body>

<section class="sheet letterhead">
  <svg class="decor" viewBox="0 0 552 784" aria-hidden="true">
    <circle cx="0" cy="0" r="120" fill="var(--green)"/>
    <circle cx="72" cy="52" r="40" fill="var(--paper)"/>
    <circle cx="72" cy="52" r="33" fill="var(--blue)"/>
    <circle cx="470" cy="545" r="240" fill="var(--pale-green)"/>
    <circle cx="344" cy="540" r="100" fill="var(--paper)"/>
    <circle cx="344" cy="540" r="88" fill="var(--pale-blue)"/>
  </svg>
  <div class="brand">
    <div class="brand__row"><span class="brand__dot"></span><span class="brand__name">The Brightway Surgery</span></div>
    <span class="brand__tagline">Friendly Local Care<br>Close To Home</span>
  </div>
  <div class="contact">
    Phone : 02 9000 4172<br>
    email : hi@thebrightwaysurgery.com.au<br>
    Website : www.thebrightwaysurgery.com.au
  </div>
  <footer class="letterhead__footer">
    <span>Maplewood</span>
    <span>The Brightway Surgery (Inside Greenleaf Pharmacy)</span>
    <span>Shop 4, Maplewood Village, 18 - 24 Harrow Parkway, Maplewood 2150</span>
  </footer>
</section>

<section class="sheet card-details">
  <div class="brand">
    <div class="brand__row"><span class="brand__dot"></span><span class="brand__name">The Brightway<br>Surgery</span></div>
    <span class="brand__tagline">Friendly Local Care<br>Close To Home</span>
  </div>
  <span class="card-details__rule"></span>
  <div class="card-details__text">
    <p>Maplewood<br>The Brightway Surgery (Inside Greenleaf Pharmacy)<br>Shop 4, Maplewood Village<br>18 - 24 Harrow Parkway<br>Maplewood 2150</p>
    <p>Phone 02 9000 4172<br>email: hi@thebrightwaysurgery.com.au<br>Website: www.thebrightwaysurgery.com.au</p>
  </div>
  <span class="card-details__band"></span>
</section>

<section class="sheet card-front">
  <svg class="decor" viewBox="0 0 498 256" aria-hidden="true">
    <circle cx="0" cy="0" r="110" fill="var(--green)"/>
    <circle cx="62" cy="48" r="34" fill="var(--paper)"/>
    <circle cx="62" cy="48" r="28" fill="var(--blue)"/>
    <circle cx="498" cy="256" r="90" fill="var(--green)"/>
    <circle cx="440" cy="218" r="26" fill="var(--paper)"/>
    <circle cx="440" cy="218" r="21" fill="var(--blue)"/>
  </svg>
  <div class="brand">
    <div class="brand__row"><span class="brand__dot"></span><span class="brand__name">The Brightway<br>Surgery</span></div>
    <span class="brand__tagline">Friendly Local Care<br>Close To Home</span>
  </div>
</section>

<section class="sheet comp-slip">
  <svg class="decor" viewBox="0 0 558 268" aria-hidden="true">
    <circle cx="20" cy="268" r="110" fill="var(--pale-green)"/>
    <circle cx="62" cy="240" r="38" fill="var(--paper)"/>
    <circle cx="62" cy="240" r="32" fill="var(--pale-blue)"/>
  </svg>
  <span class="comp-slip__title">WITH COMPLIMENTS</span>
  <div class="brand">
    <div class="brand__row"><span class="brand__dot"></span><span class="brand__name">The Brightway<br>Surgery</span></div>
    <span class="brand__tagline">Friendly Local Care<br>Close To Home</span>
  </div>
  <div class="contact">
    Phone : 02 9000 4172<br>
    email : hi@thebrightwaysurgery.com.au<br>
    Website : www.thebrightwaysurgery.com.au
  </div>
  <div class="comp-slip__address">
    Maplewood<br>
    The Brightway Surgery (Inside Greenleaf Pharmacy)<br>
    Shop 4, Maplewood Village, 18 - 24 Harrow Parkway, Maplewood 2150
  </div>
</section>

</body>
</html>
```